Executive Taxi firm with Chauffeur service Website

I have my domain name registered and I have started to work on my site but I am struggling. I am just about to get a logo for the company and need a web site that clearly represents the fact we are an executive/luxury brand in private hire vehicles. We offer airport transfers, train station transfers, seaport transfers, holiday transfers and business to business pick up and drop off.

Target Market(s)

Corporate people, holidaymakers looking for a luxury start their holiday. VIPs' and celebrities.

Number of Pages Required

5+ page

Font styles to use
Serif
Sans Serif
Decorative
Script

Colors

Designer to choose colors to be used in the design.

Requirements
Must have
• Home Page, Services, About Us, VIP and Contact us
• Please see www.brookvane.co.uk I have started it but not happy with it at all.
Nice to have
• Booking form or enquiry form.

```html
<!DOCTYPE html>
<html lang="en">
<head>
<meta charset="utf-8">
<title>Brookvane Travel – Executive Private Hire</title>
<link href="https://fonts.googleapis.com/css2?family=Open+Sans:wght@400;600;700;800&display=swap" rel="stylesheet">
<style>
:root{
  --gold:#f7b500;
  --gold-soft:#ffd04d;
  --ink:#1e1e1e;
  --text:#3a3a3a;
  --muted:#8a8a8a;
  --line:#dcdcdc;
  --canvas:#f2f2f2;
  --footer:#2b2b2b;
  --white:#ffffff;
}
*{margin:0;padding:0;box-sizing:border-box}
html,body{width:1200px;height:2564px;overflow:hidden}
body{background:var(--canvas);font-family:"Open Sans",Arial,sans-serif;color:var(--text)}
.page{position:absolute;left:48px;top:120px;width:1106px;height:2244px;background:var(--white);box-shadow:0 6px 30px rgba(0,0,0,.18);overflow:hidden}
.abs{position:absolute}

/* header */
.brand{left:174px;top:30px;font-size:22px;line-height:24px;font-weight:700;color:var(--gold)}
.brand-footer{left:103px;top:36px;font-size:24px;line-height:27px;font-weight:700;color:var(--white)}
.header-phone{left:738px;top:36px;display:flex;align-items:center;gap:8px;font-size:15px;font-weight:600;color:var(--ink)}
.social{left:904px;top:38px;display:flex;gap:10px}
.social span{width:18px;height:18px;border:1.5px solid #b5b5b5;border-radius:50%}
.nav-rule{left:326px;top:72px;width:676px;height:1px;background:var(--gold)}
.nav{left:326px;top:80px;font-size:11.5px;color:var(--text)}
.nav a{color:inherit;text-decoration:none;position:absolute;white-space:nowrap}
.nav .active{font-weight:700;color:var(--ink)}
.nav .active::before{content:"";position:absolute;left:-18px;top:-9px;width:62px;height:4px;background:var(--gold)}
.account{left:858px;top:81px;font-size:10.5px;font-weight:700;color:var(--gold);letter-spacing:.3px}

/* hero */
.hero{left:0;top:115px;width:1106px;height:504px;background:linear-gradient(100deg,#0d0d0d 0%,#2a2a2a 45%,#1a1a1a 70%,#3b3b3b 100%)}
.hero-sub{left:174px;top:232px;font-size:23px;font-weight:600;color:var(--gold)}
.hero-sub-rule{left:174px;top:274px;width:100px;height:2px;background:var(--gold)}
.hero-title{left:174px;top:283px;font-size:54px;line-height:54px;font-weight:700;color:var(--white);letter-spacing:-.5px}
.btn{display:flex;align-items:center;justify-content:center;background:var(--gold);border-radius:5px;font-weight:600;color:var(--ink)}
.hero-btn{left:174px;top:413px;width:144px;height:36px;font-size:17px}

/* app visual */
.app-visual{left:560px;top:529px;width:420px;height:540px;border-radius:24px;background:linear-gradient(150deg,#f4f4f4 0%,#d9d9d9 35%,#f2c94c 70%,#f7b500 100%)}

/* about */
.section-title{font-size:22px;font-weight:600;color:var(--gold)}
.about-title{left:174px;top:690px}
.about-rule{left:174px;top:727px;width:50px;height:1px;background:var(--gold)}
.about-copy{left:174px;top:743px;width:340px;font-size:11.4px;line-height:17.6px;color:var(--text)}
.about-copy p+p{margin-top:17px}
.about-btn{left:174px;top:1034px;width:144px;height:34px;font-size:13px;font-weight:400}
.deco-ring{left:62px;top:880px;width:46px;height:46px;border:6px solid #e7e7e7;border-radius:50%}
.deco-dot{left:112px;top:944px;width:34px;height:34px;border-radius:50%;background:#ececec}
.deco-plus{left:0;top:880px;width:20px;height:20px}
.deco-line1{left:417px;top:1052px;width:79px;height:3px;background:#dadada}
.deco-line2{left:590px;top:1082px;width:44px;height:3px;background:#dadada}

/* how it works */
.steps-band{left:0;top:1210px;width:1106px;height:477px;background:linear-gradient(100deg,#7c6a2a 0%,#a08833 45%,#8e7a2e 75%,#b39a3e 100%)}
.steps-title{left:174px;top:1257px}
.step{left:191px;display:flex;gap:14px;align-items:flex-start}
.step-num{font-size:36px;line-height:34px;font-weight:400;color:var(--white);width:20px}
.step-text{width:270px;font-size:10.6px;line-height:12.4px;color:var(--white);padding-top:4px}

/* booking form */
.booking{left:557px;top:1167px;width:389px;height:452px;background:rgba(222,214,188,.88);border-bottom:3px solid var(--gold)}
.booking-head{height:43px;background:var(--gold);display:flex;align-items:center;justify-content:center;font-size:16px;font-weight:600;color:var(--ink)}
.field{position:absolute;height:29px;background:var(--white);border:1px solid #d6d6d6;border-radius:3px;font-size:11px;color:var(--muted);display:flex;align-items:center;padding-left:10px}
.field.addon{padding-left:0}
.field .prefix{width:40px;height:100%;border-right:1px solid #d6d6d6;display:flex;align-items:center;justify-content:center;background:#f3f3f3;color:#777}
.field .value{padding-left:10px}
.label{position:absolute;font-size:10.5px;color:#444}
.submit{left:123px;top:325px;width:144px;height:36px;font-size:12px;font-weight:400}

/* faq */
.faq-title{left:0;top:1755px;width:1106px;text-align:center;font-size:19px;font-weight:700;color:var(--gold)}
.faq{left:318px;top:1807px;width:516px}
.faq-q{height:29px;display:flex;align-items:center;gap:12px;padding-left:12px;font-size:11px;background:#efefef;color:#666;margin-bottom:4px}
.faq-q .sign{width:14px;color:var(--gold);font-size:18px;font-weight:400;text-align:center}
.faq-q.open{height:31px;background:var(--gold);color:var(--white);margin-bottom:0}
.faq-q.open .sign{color:var(--white)}
.faq-a{height:62px;padding:10px 12px;font-size:10.6px;line-height:12.8px;color:var(--ink);border:1px solid #ececec;border-top:none;margin-bottom:4px}

/* footer */
.footer{left:0;top:2111px;width:1106px;height:133px;background:var(--footer)}
.foot-head{font-size:11px;font-weight:700;color:var(--gold)}
.foot-text{font-size:13px;line-height:16px;color:var(--white)}
.newsletter{left:583px;top:75px;width:376px;height:29px;border:1.5px solid var(--gold);border-radius:8px;display:flex;overflow:hidden}
.newsletter .input{flex:1;font-size:12px;font-style:italic;color:#aaa;display:flex;align-items:center;padding-left:14px;letter-spacing:1px}
.newsletter .go{width:116px;background:var(--gold);font-size:11px;font-weight:600;color:var(--ink);display:flex;align-items:center;justify-content:center}
</style>
</head>
<body>
<div class="page">

  <!-- header -->
  <div class="abs brand">Brookvane<br>Travel</div>
  <div class="abs header-phone">
    <svg width="24" height="24" viewBox="0 0 24 24"><circle cx="12" cy="12" r="11" fill="#1e1e1e"/><path d="M8 7c1 0 1.6 2 1.4 2.6l-.8.8c.5 1.3 1.7 2.5 3 3l.8-.8c.6-.2 2.6.4 2.6 1.4 0 1-1 2-2 2-3.5 0-7-3.5-7-7 0-1 1-2 2-2z" fill="#fff"/></svg>
    <span>07700 900418</span>
  </div>
  <div class="abs social"><span></span><span></span></div>
  <div class="abs nav-rule"></div>
  <nav class="abs nav">
    <a class="active" style="left:18px">Home</a>
    <a style="left:88px">About Us</a>
    <a style="left:170px">Services</a>
    <a style="left:238px">How It Works</a>
    <a style="left:344px">Contact Us</a>
  </nav>
  <div class="abs account">LOGIN &nbsp;|&nbsp; REGISTER</div>

  <!-- hero -->
  <div class="abs hero" role="img" aria-label="Chauffeur opening the rear door of a black executive car"></div>
  <div class="abs hero-sub">Private Hire, Chauffeur and taxi service</div>
  <div class="abs hero-sub-rule"></div>
  <h1 class="abs hero-title">EXECUTIVE BROOKVANE<br>TRAVEL</h1>
  <div class="abs btn hero-btn">BOOK NOW!</div>

  <!-- about -->
  <svg class="abs deco-plus" viewBox="0 0 20 20"><path d="M10 0v20M0 10h20" stroke="#e2e2e2" stroke-width="3"/></svg>
  <div class="abs deco-ring"></div>
  <div class="abs deco-dot"></div>
  <h2 class="abs section-title about-title">Always here for you</h2>
  <div class="abs about-rule"></div>
  <div class="abs about-copy">
    <p>We provide airport transfers to and from all major UK airports, seaports, train station transfers and an executive business to business transfer service. Whether you have an individual or group transfer request, our company-owned fleet offers a choice of options to suit your needs, from luxury saloons and SUV's to 9-seat luxury transporters.</p>
    <p>We provide a door-to-door convenience from your home, office or hotel straight to any destination of your choice. Pre-booked or last minute we aim to cover any transport requirement. Allports and train station service; All pickups from arrivals will of been briefed as to your exact pickup point, or your chauffeur will be waiting with a name board. We also track your arrival time, so you can relax safe in the knowledge we will be waiting for you whatever time your journey completes.</p>
  </div>
  <div class="abs btn about-btn">LEARN MORE</div>
  <div class="abs deco-line1"></div>
  <div class="abs deco-line2"></div>

  <div class="abs app-visual" role="img" aria-label="Smartphone showing a taxi booking app with a route map, set on soft yellow shapes"></div>

  <!-- how it works -->
  <div class="abs steps-band" role="img" aria-label="Passenger in a car using a phone, tinted gold"></div>
  <h2 class="abs section-title steps-title">How it works</h2>
  <div class="abs step" style="top:1336px"><span class="step-num">1</span><p class="step-text">Lorem ipsum dolor sit amet, consectetur adipiscing elit, sed do eiusmod tempLorem ipsum dolor sit amet, consectetur adipiscing</p></div>
  <div class="abs step" style="top:1406px"><span class="step-num">2</span><p class="step-text">Lorem ipsum dolor sit amet, consectetur adipiscing elit, sed do eiusmod tempLorem ipsum dolor sit amet, consectetur adipiscing</p></div>
  <div class="abs step" style="top:1474px"><span class="step-num">3</span><p class="step-text">Lorem ipsum dolor sit amet, consectetur adipiscing elit, sed do eiusmod tempLorem ipsum dolor sit amet, consectetur adipiscing</p></div>
  <div class="abs step" style="top:1541px"><span class="step-num">4</span><p class="step-text">Lorem ipsum dolor sit amet, consectetur adipiscing elit, sed do eiusmod tempLorem ipsum dolor sit amet, consectetur adipiscing</p></div>

  <!-- booking form -->
  <form class="abs booking">
    <div class="booking-head">Book a Ride with Us</div>
    <div class="field" style="left:24px;top:86px;width:166px">First name</div>
    <div class="field" style="left:195px;top:86px;width:166px">Last name</div>
    <div class="field" style="left:24px;top:128px;width:285px">email@example.com</div>
    <span class="label" style="left:24px;top:170px">Telephone</span>
    <div class="field addon" style="left:24px;top:188px;width:231px"><span class="prefix">+01</span><span class="value">000-0000-000</span></div>
    <span class="label" style="left:24px;top:228px">Date</span>
    <span class="label" style="left:204px;top:228px">Time</span>
    <div class="field addon" style="left:24px;top:245px;width:166px;color:#555">
      <span class="prefix"><svg width="16" height="14" viewBox="0 0 16 14"><rect x="1" y="2" width="14" height="11" fill="none" stroke="#777"/><path d="M1 5h14M4 8h2M8 8h2M12 8h1M4 11h2M8 11h2" stroke="#777"/></svg></span><span class="value">02-11-2018</span></div>
    <div class="field addon" style="left:195px;top:245px;width:166px;color:#555">
      <span class="prefix"><svg width="16" height="16" viewBox="0 0 16 16"><circle cx="8" cy="8" r="6.5" fill="none" stroke="#777"/><path d="M8 4v4l3 2" stroke="#777" fill="none"/></svg></span><span class="value">2:00pm</span></div>
    <div class="abs btn submit">SUBMIT</div>
  </form>

  <!-- faq -->
  <h2 class="abs faq-title">FAQs</h2>
  <div class="abs faq">
    <div class="faq-q open"><span class="sign">&minus;</span>Lorem ipsum dolor sit amet, consectetur adipiscing elit, sed do</div>
    <div class="faq-a">Lorem ipsum dolor sit amet, consectetur adipiscing elit, sed do eiusmod tempLorem ipsum dolor sit amet, consectetur adipiscing elit, sed do eiusmod temp Lorem ipsum dolor sit amet, consectetur</div>
    <div class="faq-q"><span class="sign">+</span>Lorem ipsum dolor sit amet, consectetur adipiscing elit, sed do</div>
    <div class="faq-q"><span class="sign">+</span>Lorem ipsum dolor sit amet, consectetur adipiscing elit, sed do</div>
    <div class="faq-q"><span class="sign">+</span>Lorem ipsum dolor sit amet, consectetur adipiscing elit, sed do</div>
    <div class="faq-q"><span class="sign">+</span>Lorem ipsum dolor sit amet, consectetur adipiscing elit, sed do</div>
  </div>

  <!-- footer -->
  <footer class="abs footer">
    <div class="abs brand-footer">Brookvane<br>Travel</div>
    <div class="abs foot-head" style="left:366px;top:30px">GET IN TOUCH</div>
    <div class="abs foot-text" style="left:366px;top:54px">07700 900418<br>info@brookvane.co.uk</div>
    <div class="abs foot-head" style="left:584px;top:30px">STAY CONNECTED</div>
    <div class="abs foot-text" style="left:584px;top:52px">Join our newsletter and find out more.</div>
    <div class="abs newsletter"><span class="input">Your &nbsp;e-mail</span><span class="go">SUBSCRIBE ME</span></div>
  </footer>

</div>
</body>
</html>
```